Halvercott Orthodontics business card

Using our existing logo (created with ArtFolio), please create a tasteful, contemporary business card. We are father and daughter orthodontists specializing in braces, clarafit, etc to design healthy, beautiful smiles for children, adolescents, and adults. We would like the design to be family-friendly but not childish.
The final design should include all of the information without looking cluttered (I hope! If necessary to achieve an optimal design, please consider making the card double-sided)
Purple, black, silver on a white card
Please include the following information:
Halvercott Orthodontics (logo)
Marguerite L. Halvercott, DMD
Douglas R. Halvercott, DMD

312 Bramblewood Street
North Andover, MA 01899
978.555.0142

847C Quarry Hollow Street
Methuen, MA 01898
978.555.0187

email frontdesk@halvercottortho.example
website www.halvercottortho.example

```html
<!DOCTYPE html>
<html lang="en">
<head>
<meta charset="utf-8">
<title>Halvercott Orthodontics business card</title>
<link rel="stylesheet" href="https://fonts.googleapis.com/css2?family=Old+Standard+TT:wght@400&display=swap">
<style>
  :root {
    --backdrop: #b39ac8;
    --card: #ffffff;
    --purple: #6a2c91;
    --ink: #111111;
    --silver: #7c7c7c;
    --icon: #ffffff;
  }
  * { margin: 0; padding: 0; box-sizing: border-box; }
  html, body { width: 1200px; height: 1200px; overflow: hidden; }
  body {
    background: var(--backdrop);
    font-family: "Old Standard TT", "Century Schoolbook", serif;
    position: relative;
  }
  .card {
    position: absolute;
    left: 169px;
    width: 859px;
    height: 503px;
    background: var(--card);
  }
  .card--front { top: 72px; }
  .card--back { top: 624px; }

  .brand-name {
    position: absolute;
    color: var(--purple);
    font-weight: 400;
    white-space: nowrap;
  }
  .card--front .brand-name {
    left: 52px;
    top: 170px;
    font-size: 34px;
    line-height: 1.2;
  }

  .doctors {
    position: absolute;
    right: 37px;
    top: 70px;
    text-align: right;
    color: var(--ink);
    font-size: 30px;
    line-height: 39px;
  }

  .contact-row {
    position: absolute;
    right: 0;
    height: 23px;
    display: flex;
    align-items: center;
    gap: 20px;
  }
  .contact-row__text {
    color: var(--silver);
    font-size: 17px;
    letter-spacing: 0.2px;
    white-space: nowrap;
  }
  .contact-row__tab {
    width: 66px;
    height: 23px;
    background: var(--purple);
    display: flex;
    align-items: center;
    padding-left: 18px;
  }
  .contact-row__tab svg { width: 13px; height: 13px; display: block; }

  .lockup {
    position: absolute;
    left: 50%;
    top: 50%;
    transform: translate(-50%, -50%);
    display: flex;
    align-items: center;
    gap: 26px;
  }
  .lockup__dot {
    width: 62px;
    height: 62px;
    border-radius: 50%;
    background: var(--purple);
    flex: none;
  }
  .card--back .brand-name {
    position: static;
    font-size: 54px;
    line-height: 1;
  }
</style>
</head>
<body>

<section class="card card--front">
  <div class="brand-name">Halvercott<br>Orthodontics</div>

  <div class="doctors">
    <p>Marguerite L. Halvercott, DMD</p>
    <p>Douglas R. Halvercott, DMD</p>
  </div>

  <div class="contact-row" style="top:198px">
    <span class="contact-row__text">frontdesk@halvercottortho.example</span>
    <span class="contact-row__tab">
      <svg viewBox="0 0 16 16" fill="none" stroke="var(--icon)" stroke-width="1.6"><rect x="1.5" y="3.5" width="13" height="9" fill="var(--icon)" stroke="none"/><path d="M1.5 3.8 8 8.8l6.5-5" stroke="var(--purple)"/></svg>
    </span>
  </div>
  <div class="contact-row" style="top:233px">
    <span class="contact-row__text">www.halvercottortho.example</span>
    <span class="contact-row__tab">
      <svg viewBox="0 0 16 16" fill="none" stroke="var(--icon)" stroke-width="1.4"><circle cx="8" cy="8" r="6.5"/><ellipse cx="8" cy="8" rx="2.8" ry="6.5"/><path d="M1.5 8h13"/></svg>
    </span>
  </div>

  <div class="contact-row" style="top:304px">
    <span class="contact-row__text">978.555.0142</span>
    <span class="contact-row__tab">
      <svg viewBox="0 0 16 16" fill="var(--icon)"><path d="M3.6 1.5 6 4.2 4.8 6a8.5 8.5 0 0 0 5.2 5.2l1.8-1.2 2.7 2.4-1.3 2.1C7.5 14.5 1.5 8.5 1.5 2.8z"/></svg>
    </span>
  </div>
  <div class="contact-row" style="top:338px">
    <span class="contact-row__text">312 Bramblewood Street, North Andover, MA 01899</span>
    <span class="contact-row__tab">
      <svg viewBox="0 0 16 16" fill="var(--icon)"><path d="M8 1a5 5 0 0 0-5 5c0 3.6 5 9 5 9s5-5.4 5-9a5 5 0 0 0-5-5zm0 7a2 2 0 1 1 0-4 2 2 0 0 1 0 4z"/></svg>
    </span>
  </div>

  <div class="contact-row" style="top:391px">
    <span class="contact-row__text">978.555.0187</span>
    <span class="contact-row__tab">
      <svg viewBox="0 0 16 16" fill="var(--icon)"><path d="M3.6 1.5 6 4.2 4.8 6a8.5 8.5 0 0 0 5.2 5.2l1.8-1.2 2.7 2.4-1.3 2.1C7.5 14.5 1.5 8.5 1.5 2.8z"/></svg>
    </span>
  </div>
  <div class="contact-row" style="top:425px">
    <span class="contact-row__text">847C Quarry Hollow Street, Methuen, MA 01898</span>
    <span class="contact-row__tab">
      <svg viewBox="0 0 16 16" fill="var(--icon)"><path d="M8 1a5 5 0 0 0-5 5c0 3.6 5 9 5 9s5-5.4 5-9a5 5 0 0 0-5-5zm0 7a2 2 0 1 1 0-4 2 2 0 0 1 0 4z"/></svg>
    </span>
  </div>
</section>

<section class="card card--back">
  <div class="lockup">
    <span class="lockup__dot"></span>
    <span class="brand-name">Halvercott Orthodontics</span>
  </div>
</section>

</body>
</html>
```